Business Card Design for Kidvale (Hires out childrens play areas)

Looking to have a business card designed for a company we just bought. The company rents out childrens play areas.

I have uploaded a couple of examples of the kind of business card style I like. Here are two more examples:

https://quorvastudio.nz/project/bright-romp-branding/
https://imgvaultcdn.com/design_img/8841052/302917/302917_5518203_8841052_b73e19a2_image.jpg

I think a white card will be best due to all the colours in the logo.

Size we require: 3.75" x 2.25" (horizontally orientated) with a 0.125" bleed

Uploaded is two versions of our logo.

Details for the card:
1. My name: Liam Verster
2. Title: Managing Director
3. Phone no: 021 563 417
4. Email: liam@kidvale.co.nz
5. URL: www.kidvale.co.nz
6. Address:
PO Box 318625
Fernlea, Auckland

Let me know if you need anything else.

Target Market(s)

Hospitals, doctors surgeries, bed shops, etc.

Contact Information for Business Card

Details for the card:
1. My name: Liam Verster
3. Phone no: 021 563 417
5. URL: www.kidvale.co.nz
6. Address:
PO Box 318625
Fernlea, Auckland

Requirements
Should not have
• Not too busy.

```html
<!DOCTYPE html>
<html lang="en">
<head>
<meta charset="utf-8">
<title>Kidvale Business Card</title>
<link rel="stylesheet" href="https://fonts.googleapis.com/css2?family=Work+Sans:wght@400;500;600&display=swap">
<style>
  :root {
    --backdrop: #2b2b2b;
    --card: #1f1f1f;
    --card-sheen: #2a2a2a;
    --accent: #f7941d;
    --ink: #f2f2f2;
    --link: #2d7fd3;
    --rule: #e6e6e6;
  }
  * { box-sizing: border-box; margin: 0; padding: 0; }
  html, body {
    width: 1200px;
    height: 900px;
    overflow: hidden;
    background: var(--backdrop);
    font-family: "Work Sans", sans-serif;
    color: var(--ink);
  }
  .stage { position: relative; width: 1200px; height: 900px; }
  .card {
    position: absolute;
    left: 250px;
    width: 700px;
    height: 420px;
    background: radial-gradient(ellipse at 70% 40%, var(--card-sheen), var(--card) 70%);
    border-bottom: 6px solid var(--accent);
    overflow: hidden;
  }
  .card--front { top: 20px; }
  .card--back { top: 460px; }

  .brand {
    position: absolute;
    display: flex;
    align-items: center;
    gap: 12px;
    font-weight: 600;
    color: var(--accent);
  }
  .brand__dot {
    width: 22px;
    height: 22px;
    border-radius: 50%;
    background: var(--accent);
  }
  .card--front .brand {
    left: 50%;
    top: 50%;
    transform: translate(-50%, -55%);
    font-size: 64px;
  }
  .card--back .brand {
    left: 70px;
    top: 150px;
    font-size: 50px;
  }

  .divider {
    position: absolute;
    left: 385px;
    top: 110px;
    width: 2px;
    height: 190px;
    background: var(--rule);
  }
  .details {
    position: absolute;
    left: 415px;
    top: 100px;
    font-size: 16px;
    line-height: 1.35;
    letter-spacing: 0.04em;
  }
  .details__name {
    font-size: 30px;
    font-weight: 500;
    color: var(--accent);
    letter-spacing: 0.05em;
    line-height: 1.1;
  }
  .details__title { margin-bottom: 14px; }
  .details__address { margin-bottom: 12px; }
  .contact { list-style: none; }
  .contact li { display: flex; align-items: center; gap: 10px; }
  .contact svg { width: 13px; height: 13px; flex: none; }
  .contact__site-name { color: var(--link); }
</style>
</head>
<body>
<main class="stage">
  <section class="card card--front">
    <div class="brand"><span class="brand__dot"></span>Kidvale</div>
  </section>

  <section class="card card--back">
    <div class="brand"><span class="brand__dot"></span>Kidvale</div>
    <div class="divider"></div>
    <div class="details">
      <p class="details__name">Liam Verster</p>
      <p class="details__title">Managing Director</p>
      <p class="details__address">PO Box 318625<br>Fernlea, Auckland</p>
      <ul class="contact">
        <li>
          <svg viewBox="0 0 16 16" aria-hidden="true"><path d="M4 1.5l2.5 3-1.5 2a8 8 0 0 0 4.5 4.5l2-1.5 3 2.5-1.5 2.5C7 14 2 9 1.5 3z" fill="none" stroke="#f7941d" stroke-width="1.5" stroke-linejoin="round"/></svg>
          021 563 417
        </li>
        <li>
          <svg viewBox="0 0 16 16" aria-hidden="true"><rect x="1.5" y="3.5" width="13" height="9" fill="none" stroke="#f7941d" stroke-width="1.5"/><path d="M1.5 3.5L8 9l6.5-5.5" fill="none" stroke="#f7941d" stroke-width="1.5"/></svg>
          liam@kidvale.co.nz
        </li>
        <li>
          <svg viewBox="0 0 16 16" aria-hidden="true"><circle cx="8" cy="8" r="6.5" fill="none" stroke="#f7941d" stroke-width="1.4"/><ellipse cx="8" cy="8" rx="3" ry="6.5" fill="none" stroke="#f7941d" stroke-width="1.2"/><path d="M1.5 8h13" stroke="#f7941d" stroke-width="1.2"/></svg>
          <span>www.<span class="contact__site-name">kidvale</span>.co.nz</span>
        </li>
      </ul>
    </div>
  </section>
</main>
</body>
</html>
```